Home page makeover

Take my existing home page, www.maplecrestharborline.com and redesign layout to look more current considering today's touch design prevalence.
Reuse existing elements or suggest improved ones if available.
I generally have average CSS and HTML skills using div containers, defining lists and using columns to create the code to support the layout.
Updates
Just wanted to send out a quick message to thank all of you for your submissions. Many of you offered nice designs, but unfortunately could only choose one.
Target Market(s)
Generally targeting individuals with some assets for retirement. Basically your average working professional or business owner.
Industry/Entity Type
It Support
Look and feel
Each slider illustrates characteristics of the customer's brand and the style your logo design should communicate.

```html
<!DOCTYPE html>
<html lang="en">
<head>
<meta charset="utf-8">
<title>Maplecrest Harborline – Home</title>
<link href="https://fonts.googleapis.com/css2?family=Mulish:wght@400;600;700;800&display=swap" rel="stylesheet">
<style>
:root{
  --green:#1f8a1f;
  --green-dark:#0f6b12;
  --lime:#8cc63f;
  --lime-dark:#6ea42a;
  --ink:#1d1d1d;
  --text:#333;
  --muted:#777;
  --rule:#cfcfcf;
  --soft:#f8f8f8;
  --white:#fff;
}
*{box-sizing:border-box;margin:0;padding:0}
html,body{width:1052px;height:1200px;overflow:hidden;background:var(--white)}
body{font-family:"Mulish",sans-serif;color:var(--text);position:relative}
.wrap{width:894px;margin:0 auto;position:relative}

.site-header{height:106px}
.site-header .wrap{height:106px;display:flex;align-items:center}
.brand{display:flex;align-items:center;gap:10px;color:var(--green-dark);font-weight:800;font-size:30px;letter-spacing:.5px}
.brand-mark{width:34px;height:34px;background:var(--green);border-radius:4px}
.social{margin-left:auto;display:flex;gap:4px}
.social span{width:25px;height:25px;border-radius:50%;display:block}
.social .s1{background:#3b5998}.social .s2{background:#3aa6dd}.social .s3{background:#d43b2b}

.main-nav{height:33px;background:linear-gradient(#1f8e1f,#127212)}
.main-nav ul{list-style:none;display:flex;height:33px}
.main-nav a{display:block;height:33px;line-height:33px;padding:0 11px;color:var(--white);text-decoration:none;font-size:13.5px}
.main-nav a.active{background:#30a530}

.hero{height:295px;position:relative;background:linear-gradient(90deg,#2a2a2a,#6e6e6e 45%,#8a8a8a 60%,#3c3c3c)}
.hero .wrap{height:295px}
.video{position:absolute;left:0;top:17px;width:379px;height:263px;background:#111}
.video-title{position:absolute;left:9px;top:6px;color:#ddd;font-size:9px}
.video-frame{position:absolute;left:47px;top:24px;width:286px;height:213px;background:linear-gradient(135deg,#555,#ddd 55%,#f2f2f2)}
.play{position:absolute;left:160px;top:110px;width:61px;height:42px;border-radius:9px;background:#222}
.play::after{content:"";position:absolute;left:24px;top:13px;border-left:16px solid #fff;border-top:8px solid transparent;border-bottom:8px solid transparent}
.video-label{position:absolute;left:56px;top:155px;color:#fff;font-weight:800;font-style:italic;font-size:38px}
.video-bar{position:absolute;left:0;bottom:0;width:100%;height:24px;background:#1a1a1a;border-top:3px solid #444;color:#ccc;font-size:8px;padding:5px 0 0 66px}
.offer{position:absolute;left:405px;top:88px;color:var(--white);font-weight:800;font-size:24px;line-height:36px;text-shadow:0 1px 3px rgba(0,0,0,.7)}
.btn-signup{position:absolute;left:406px;top:174px;width:136px;height:53px;background:var(--lime);border-bottom:4px solid var(--lime-dark);border-radius:3px;color:var(--white);font-weight:800;font-size:24px;text-align:center;line-height:50px;text-shadow:0 1px 2px rgba(0,0,0,.4)}

.steps{padding-top:13px;height:226px}
.steps .wrap{display:flex;justify-content:space-between}
.step{width:286px;height:190px;border:1px solid #ddd;border-radius:3px;padding:10px 13px;background:var(--white);box-shadow:0 1px 3px rgba(0,0,0,.08)}
.step-photo{position:relative;height:168px}
.step-photo span{position:absolute;left:0;right:0;bottom:0;height:32px;background:rgba(0,0,0,.55);color:var(--white);font-weight:800;font-size:24px;line-height:36px;padding-left:11px}
.p1{background:linear-gradient(135deg,#7a8a70,#e6e2d6)}
.p2{background:linear-gradient(135deg,#3a3a3a,#e5e5e5)}
.p3{background:linear-gradient(180deg,#8fb4d8,#b99a6a 60%,#5b4a36)}

.features{background:var(--soft);height:271px;padding-top:17px}
.section-title{font-size:23.5px;font-weight:800;color:var(--ink)}
.features .section-title{border-bottom:1px solid var(--rule);padding-bottom:6px}
.feature-cols{display:flex;margin-top:11px}
.feature-cols ul{list-style:none}
.feature-cols .col-left{width:482px;flex-shrink:0;padding-right:30px}
.feature-cols .col-right{flex:1}
.feature-cols li{position:relative;padding-left:22px;font-size:15px;line-height:19px;margin-bottom:19px;color:#222}
.feature-cols li::before{content:"";position:absolute;left:0;top:3px;width:14px;height:14px;border-radius:50%;background:var(--lime)}
.feature-cols li::after{content:"";position:absolute;left:5px;top:6.5px;border-left:6px solid #fff;border-top:3.5px solid transparent;border-bottom:3.5px solid transparent}

.testimonials{height:200px;padding-top:16px}
.testimonials-head{display:flex;justify-content:space-between;align-items:center}
.arrows{display:flex;gap:3px}
.arrows span{width:21px;height:21px;border-radius:50%;background:#9a9a9a;position:relative}
.arrows span::after{content:"";position:absolute;top:6px;border-top:4.5px solid transparent;border-bottom:4.5px solid transparent}
.arrows .prev::after{left:6px;border-right:7px solid #fff}
.arrows .next::after{left:8px;border-left:7px solid #fff}
.quotes{display:flex;justify-content:space-between;margin-top:11px}
.quote{width:289px;height:125px;border:1px solid #ddd;border-radius:3px;box-shadow:0 1px 4px rgba(0,0,0,.1);padding:26px 17px;font-size:15px;line-height:23px;color:#222}
.quote cite{font-style:normal;color:var(--muted)}

.site-footer{position:absolute;left:0;top:1131px;width:1052px;height:69px;background:var(--green-dark)}
.site-footer .wrap{display:flex;padding-top:17px}
.footer-nav{display:flex;gap:11px;list-style:none}
.footer-nav a{color:var(--white);text-decoration:none;font-size:13.5px}
.copyright{color:#cfe6cf;font-size:10.5px;margin-top:7px}
.site-footer .social{margin-top:5px;gap:5px}
.site-footer .social span{background:var(--white)}
</style>
</head>
<body>
<header class="site-header">
  <div class="wrap">
    <div class="brand"><span class="brand-mark"></span>Maplecrest Harborline</div>
    <div class="social" aria-label="Social links"><span class="s1"></span><span class="s2"></span><span class="s3"></span></div>
  </div>
</header>

<nav class="main-nav">
  <div class="wrap">
    <ul>
      <li><a class="active" href="#">HOME</a></li>
      <li><a href="#">ABOUT</a></li>
      <li><a href="#">SIGN UP</a></li>
      <li><a href="#">CONTACT</a></li>
      <li><a href="#">SIGN IN</a></li>
    </ul>
  </div>
</nav>

<section class="hero" role="img" aria-label="Black and white photo of an older man with raised fist, seen from behind">
  <div class="wrap">
    <div class="video">
      <span class="video-title">Demo.wmv</span>
      <div class="video-frame" role="img" aria-label="Laptop keyboard with reading glasses"></div>
      <span class="video-label">Plan</span>
      <div class="play"></div>
      <div class="video-bar">0:00 / 0:28</div>
    </div>
    <p class="offer">Only $19.99 For a One Year Membership<br>Only $9.99 Per Year After That</p>
    <a class="btn-signup">Sign Up</a>
  </div>
</section>

<section class="steps">
  <div class="wrap">
    <div class="step"><div class="step-photo p1" role="img" aria-label="Cash, pen and stock charts"><span>Identify</span></div></div>
    <div class="step"><div class="step-photo p2" role="img" aria-label="Laptop keyboard with glasses"><span>Plan</span></div></div>
    <div class="step"><div class="step-photo p3" role="img" aria-label="Hammock on a porch by the sea"><span>Retire</span></div></div>
  </div>
</section>

<section class="features">
  <div class="wrap">
    <h2 class="section-title">Features</h2>
    <div class="feature-cols">
      <ul class="col-left">
        <li>Identify and project your retirement needs and expectations including basic living expenses, housing costs, recreation, big ticket non-recurring items, medical and nursing home care.</li>
        <li>Identify and project all your sources of retirement income including retirement savings, other savings, pension plans, Social Security, life insurance and working part-time during retirement for a period of time.</li>
      </ul>
      <ul class="col-right">
        <li>Strategize tapping into the equity of your real estate including swapping your primary residence for a different home or retirement area, or selling and renting.</li>
        <li>Produce easy to understand results featuring the Horizon Readiness Meter™.</li>
        <li>Save your work so you can return, revisit and edit your retirement plan at a later date.</li>
      </ul>
    </div>
  </div>
</section>

<section class="testimonials">
  <div class="wrap">
    <div class="testimonials-head">
      <h2 class="section-title">Testimonials</h2>
      <div class="arrows"><span class="prev"></span><span class="next"></span></div>
    </div>
    <div class="quotes">
      <blockquote class="quote">“This site is a great place to get a handle on your retirement strategy”, <cite>Dana, New Jersey</cite></blockquote>
      <blockquote class="quote">“It's the only retirement projection tool for the average user that puts it all together”, <cite>Owen, New York</cite></blockquote>
      <blockquote class="quote">“It's the only retirement projection tool for the average user that puts it all together”, <cite>Owen, New York</cite></blockquote>
    </div>
  </div>
</section>

<footer class="site-footer">
  <div class="wrap">
    <div>
      <ul class="footer-nav">
        <li><a href="#">Home</a></li>
        <li><a href="#">About</a></li>
        <li><a href="#">Sign Up</a></li>
        <li><a href="#">Contact</a></li>
        <li><a href="#">Sign In</a></li>
      </ul>
      <p class="copyright">Copyright © 2013 maplecrestharborline.com All Rights Reserved</p>
    </div>
    <div class="social" aria-label="Social links"><span></span><span></span><span></span></div>
  </div>
</footer>
</body>
</html>
```